RLT PowerPoint

I am looking for a clean, corporate PowerPoint template.

I would like the following:
- title slide
- break slide
- blank slide with title (for graphs or graphics)
- an ending slide.

Target Market(s)

Business professionals, medium to large business clients.

Requirements
Must have
• Must incorporate the RLT logo in either the header or footer

```html
<!DOCTYPE html>
<html lang="en">
<head>
<meta charset="utf-8">
<title>RLT Presentation Template</title>
<link rel="stylesheet" href="https://fonts.googleapis.com/css2?family=Alfa+Slab+One&family=Open+Sans:wght@400;600;700&family=Roboto+Condensed:wght@400&display=swap">
<style>
  :root {
    --brand-blue: #29a8e0;
    --brand-blue-deep: #1a7fc0;
    --band-dark: #1f1f1f;
    --ink: #222222;
    --paper-light: #f1f1f1;
    --paper-mid: #d9d9d9;
    --white: #ffffff;
    --rule: #2b2b2b;
  }
  * { box-sizing: border-box; margin: 0; padding: 0; }
  html, body { width: 1200px; height: 900px; overflow: hidden; background: var(--white); }
  body { position: relative; font-family: "Open Sans", Arial, sans-serif; color: var(--ink); }

  .slide {
    position: absolute;
    overflow: hidden;
    background:
      radial-gradient(ellipse at 30% 20%, rgba(255,255,255,.85), transparent 60%),
      radial-gradient(ellipse at 80% 75%, rgba(255,255,255,.6), transparent 55%),
      linear-gradient(160deg, var(--paper-light), var(--paper-mid));
  }
  .slide--title  { left: 73px;  top: 168px; width: 555px; height: 312px; }
  .slide--end    { left: 72px;  top: 517px; width: 557px; height: 312px; }
  .slide--bullet { left: 680px; top: 18px;  width: 456px; height: 255px; }
  .slide--image  { left: 679px; top: 298px; width: 457px; height: 257px; }
  .slide--graphic{ left: 680px; top: 575px; width: 456px; height: 253px; }

  .display { font-family: "Alfa Slab One", Georgia, serif; color: var(--brand-blue); letter-spacing: 1px; line-height: 1; }

  .hero-title { position: absolute; left: 0; right: 0; text-align: center; }
  .hero-title__text { font-size: 50px; }
  .hero-title__reflection {
    font-size: 50px; transform: scaleY(-1); opacity: .12; color: var(--ink);
    -webkit-mask-image: linear-gradient(to top, #000, transparent 70%);
            mask-image: linear-gradient(to top, #000, transparent 70%);
  }
  .slide--title .hero-title { top: 28px; left: 10px; }
  .slide--end .hero-title { top: 128px; }
  .slide--end .hero-title__reflection { color: var(--brand-blue); opacity: .35; margin-top: -4px; }

  .title-details {
    font-size: 11.5px; font-weight: 600; letter-spacing: .2px; color: var(--ink);
    margin: 3px 0 -2px;
  }

  .brand-seal {
    position: absolute; left: 227px; top: 149px; width: 117px; height: 117px;
    border-radius: 50%; background: var(--brand-blue);
    display: flex; align-items: center; justify-content: center;
    font-family: "Open Sans", Arial, sans-serif; font-weight: 700; font-size: 38px; color: var(--white);
  }
  .site-url { position: absolute; left: 0; right: 0; top: 282px; text-align: center; font-size: 12px; padding-right: 50px; }

  .page-tag { position: absolute; width: 50px; height: 44px; }
  .page-tag--bottom { right: 12px; bottom: 10px; }
  .page-tag--top { right: 6px; top: 2px; width: 40px; height: 42px; }
  .page-tag svg { display: block; width: 100%; height: 100%; }

  .top-rule { position: absolute; left: 6px; top: 10px; width: 410px; height: 16px; }

  .bullets { position: absolute; left: 40px; top: 38px; }
  .bullet-main { display: flex; align-items: center; gap: 7px; font-family: "Alfa Slab One", Georgia, serif; font-size: 17px; color: var(--brand-blue); }
  .bullet-sub { list-style: none; margin: 8px 0 0 37px; }
  .bullet-sub li { display: flex; align-items: center; gap: 5px; font-family: Georgia, serif; font-size: 10px; margin-bottom: 8px; text-transform: uppercase; }

  .title-band {
    position: absolute; left: 5px; right: 5px; height: 58px; background: var(--band-dark);
  }
  .slide--bullet .title-band  { top: 195px; }
  .slide--image .title-band   { top: 196px; }
  .slide--graphic .title-band { top: 193px; }
  .title-band__heading {
    position: absolute; left: 9px; top: 8px; font-size: 27px; padding-bottom: 2px;
    border-bottom: 1.5px solid var(--white);
  }
  .title-band__sub { position: absolute; top: 42px; font-size: 7.5px; color: var(--white); text-transform: uppercase; }
  .slide--bullet .title-band__sub { left: 128px; }
  .slide--image .title-band__sub, .slide--graphic .title-band__sub { left: 32px; }
  .title-band__contact { position: absolute; left: 320px; top: 22px; font-size: 4.5px; line-height: 7px; color: var(--white); text-transform: uppercase; }
  .title-band__mark {
    position: absolute; right: 4px; top: 4px; width: 61px; height: 50px; background: var(--white);
    display: flex; align-items: center; justify-content: center;
    font-family: "Open Sans", Arial, sans-serif; font-weight: 700; font-size: 20px; color: var(--brand-blue-deep);
  }

  .image-frame { position: absolute; left: 11px; top: 14px; width: 191px; height: 168px; background: var(--band-dark); }
  .image-placeholder { position: absolute; left: 4px; top: 4px; width: 158px; height: 160px; background: linear-gradient(135deg, var(--brand-blue) 55%, var(--brand-blue-deep)); }
  .image-caption {
    position: absolute; left: 166px; top: 4px; width: 20px; height: 160px;
    writing-mode: vertical-rl; transform: rotate(180deg);
    font-family: "Roboto Condensed", Arial, sans-serif; font-size: 10px; color: var(--white);
    display: flex; align-items: center; justify-content: center;
  }

  .chart-pyramid { position: absolute; left: 30px; top: 72px; width: 186px; height: 110px; }
  .chart-pie { position: absolute; left: 258px; top: 44px; width: 140px; height: 150px; }
</style>
</head>
<body>

  <!-- Title slide -->
  <section class="slide slide--title">
    <div class="hero-title">
      <div class="display hero-title__text">TITLE PAGE</div>
      <p class="title-details">DETAILS OF PRESENTATION / NAME OF PRESENTOR</p>
      <div class="display hero-title__reflection" aria-hidden="true">TITLE PAGE</div>
    </div>
    <div class="brand-seal">RLT</div>
    <p class="site-url">http://www.companysite.com/</p>
    <div class="page-tag page-tag--bottom">
      <svg viewBox="0 0 50 44"><polygon points="50,0 50,44 0,44" fill="var(--brand-blue)"/><text x="34" y="38" font-family="Alfa Slab One, serif" font-size="17" fill="#fff" text-anchor="middle">01</text></svg>
    </div>
  </section>

  <!-- Ending slide -->
  <section class="slide slide--end">
    <div class="hero-title">
      <div class="display hero-title__text">THANK YOU</div>
      <div class="display hero-title__reflection" aria-hidden="true">THANK YOU</div>
    </div>
    <div class="page-tag page-tag--bottom">
      <svg viewBox="0 0 50 44"><polygon points="50,0 50,44 0,44" fill="var(--brand-blue)"/><text x="34" y="38" font-family="Alfa Slab One, serif" font-size="19" fill="#fff" text-anchor="middle">X</text></svg>
    </div>
  </section>

  <!-- Bullet slide -->
  <section class="slide slide--bullet">
    <svg class="top-rule" viewBox="0 0 410 16"><line x1="14" y1="8" x2="410" y2="8" stroke="var(--rule)" stroke-width="1.5"/><circle cx="8" cy="8" r="6" fill="#fff" stroke="var(--rule)" stroke-width="1.3"/><rect x="5.5" y="5.5" width="5" height="5" transform="rotate(45 8 8)" fill="var(--brand-blue)"/></svg>
    <div class="page-tag page-tag--top">
      <svg viewBox="0 0 40 42"><polygon points="0,0 40,0 40,42" fill="var(--brand-blue)"/><text x="30" y="15" font-family="Alfa Slab One, serif" font-size="9" fill="#fff" text-anchor="middle">03</text></svg>
    </div>
    <div class="bullets">
      <div class="bullet-main"><svg width="18" height="18" viewBox="0 0 18 18"><polygon points="9,2 15,5.5 15,12.5 9,16 3,12.5 3,5.5" fill="none" stroke="var(--brand-blue)" stroke-width="2.6"/></svg>MAIN BULLET</div>
      <ul class="bullet-sub">
        <li><svg width="12" height="12" viewBox="0 0 12 12"><polygon points="6,1 11,3.5 11,8.5 6,11 1,8.5 1,3.5" fill="var(--brand-blue)" stroke="var(--ink)" stroke-width="1.5"/></svg>Sub bullet form</li>
        <li><svg width="12" height="12" viewBox="0 0 12 12"><polygon points="6,1 11,3.5 11,8.5 6,11 1,8.5 1,3.5" fill="var(--brand-blue)" stroke="var(--ink)" stroke-width="1.5"/></svg>Sub bullet form</li>
        <li><svg width="12" height="12" viewBox="0 0 12 12"><polygon points="6,1 11,3.5 11,8.5 6,11 1,8.5 1,3.5" fill="var(--brand-blue)" stroke="var(--ink)" stroke-width="1.5"/></svg>Sub bullet form</li>
      </ul>
    </div>
    <div class="title-band">
      <h2 class="display title-band__heading">SLIDE TITLE</h2>
      <p class="title-band__sub">Bullet form</p>
      <p class="title-band__contact">www.companysite.com<br>mail@companysite.com</p>
      <div class="title-band__mark">RLT</div>
    </div>
  </section>

  <!-- Image slide -->
  <section class="slide slide--image">
    <div class="page-tag page-tag--top">
      <svg viewBox="0 0 40 42"><polygon points="0,0 40,0 40,42" fill="var(--brand-blue)"/><text x="30" y="15" font-family="Alfa Slab One, serif" font-size="9" fill="#fff" text-anchor="middle">02</text></svg>
    </div>
    <div class="image-frame">
      <div class="image-placeholder" role="img" aria-label="Sample image area"></div>
      <p class="image-caption">sample image placement</p>
    </div>
    <div class="title-band">
      <h2 class="display title-band__heading">SLIDE TITLE</h2>
      <p class="title-band__sub">Details of slide / name of presentor</p>
      <p class="title-band__contact">www.companysite.com<br>mail@companysite.com</p>
      <div class="title-band__mark">RLT</div>
    </div>
  </section>

  <!-- Graphic slide -->
  <section class="slide slide--graphic">
    <svg class="top-rule" viewBox="0 0 410 16"><line x1="14" y1="8" x2="400" y2="8" stroke="var(--rule)" stroke-width="1.5"/><circle cx="8" cy="8" r="6" fill="#fff" stroke="var(--rule)" stroke-width="1.3"/><rect x="5.5" y="5.5" width="5" height="5" transform="rotate(45 8 8)" fill="var(--brand-blue)"/></svg>
    <div class="page-tag page-tag--top">
      <svg viewBox="0 0 40 42"><polygon points="0,0 40,0 40,42" fill="var(--brand-blue)"/><text x="30" y="15" font-family="Alfa Slab One, serif" font-size="9" fill="#fff" text-anchor="middle">04</text></svg>
    </div>
    <svg class="chart-pyramid" viewBox="0 0 186 110" role="img" aria-label="Three-level pyramid chart">
      <polygon points="84,0 102,28 66,28" fill="#8dc63f"/>
      <polygon points="66,31 102,31 110,44 58,44" fill="#71a832"/>
      <polygon points="58,32 110,32 120,64 48,64" fill="var(--brand-blue)"/>
      <polygon points="48,65 120,65 125,72 43,72" fill="var(--brand-blue-deep)"/>
      <polygon points="40,70 150,70 165,92 20,92" fill="#58595b"/>
      <polygon points="20,92 165,92 182,100 0,100 " fill="#3a3a3c"/>
      <polygon points="0,100 182,100 166,106 16,106" fill="#2a2a2a"/>
    </svg>
    <svg class="chart-pie" viewBox="-70 -70 140 150" role="img" aria-label="Seven-part pie chart">
      <g transform="translate(0,12) scale(1,.95)">
        <path d="M0,0 L64.3,14.7 A66,66 0 0 1 -64.3,14.7 Z" fill="#3a3a3c"/>
        <path d="M0,0 L64.3,14.7 A66,66 0 0 1 28.6,59.5 Z" fill="var(--brand-blue-deep)"/>
        <path d="M0,0 L28.6,59.5 A66,66 0 0 1 -28.6,59.5 Z" fill="#8c6a44"/>
      </g>
      <g transform="scale(1,.95)" stroke="#1a1a1a" stroke-width="1.4">
        <path d="M0,0 L0,-66 A66,66 0 0 1 51.6,-41.2 Z" fill="#1a8f3f"/>
        <path d="M0,0 L51.6,-41.2 A66,66 0 0 1 64.3,14.7 Z" fill="#2db36b"/>
        <path d="M0,0 L64.3,14.7 A66,66 0 0 1 28.6,59.5 Z" fill="var(--brand-blue)"/>
        <path d="M0,0 L28.6,59.5 A66,66 0 0 1 -28.6,59.5 Z" fill="#c49a6c"/>
        <path d="M0,0 L-28.6,59.5 A66,66 0 0 1 -64.3,14.7 Z" fill="#6d6e71"/>
        <path d="M0,0 L-64.3,14.7 A66,66 0 0 1 -51.6,-41.2 Z" fill="#6d6e71"/>
        <path d="M0,0 L-51.6,-41.2 A66,66 0 0 1 0,-66 Z" fill="#8dc63f"/>
        <path d="M0,0 L51.6,-41.2 A66,66 0 0 1 64.3,14.7 Z" fill="#17a89a"/>
      </g>
    </svg>
    <div class="title-band">
      <h2 class="display title-band__heading">GRAPHIC SLIDE</h2>
      <p class="title-band__sub">Details of slide / name of presentor</p>
      <p class="title-band__contact">www.companysite.com<br>mail@companysite.com</p>
      <div class="title-band__mark">RLT</div>
    </div>
  </section>

</body>
</html>
```